Banner Ad Design Project

I need 4 campaigns to have banners made, 6 banner sizes each so 24 total banners. Here are the landing pages with the messaging.

http://www.brightvalelistings.example/Oxwell-Care-Health-Insurance-48207.html

http://www.brightvalelistings.example/Marlow-Crest-Lending-48206.html
Marlow Crest Lending: Get Cash! Stay in Your Home! Then below in smaller lettering Find out if a reverse mortgage is right for you!

http://www.brightvalelistings.example/Vexmo-Direct-48205.html
Vexmo: Is Your Family Protected? Then in smaller lettering Call NOW for a FREE home security evaluation

http://www.brightvalelistings.example/LedgerSafeHelp-48217.html
Ledger Safe Helpers: We’ll help solve your IRS tax problems then in smaller lettering, Call today to find out how we can help!

Need to get done asap. Much more work can be following right after. Here are the sizes

300 X 50
300x250
320 X50
216 X36
168 X 28
120 X 20
Updates

I need final designs to choose from right now. I need to make a selection to get the banners done immediately. thanks

Industry/Entity Type

Security

Requirements
Must have
• Phone number call to action

```html
<!DOCTYPE html>
<html lang="en">
<head>
<meta charset="utf-8">
<title>Marlow Crest Lending – Reverse Mortgage Banner Set</title>
<link href="https://fonts.googleapis.com/css2?family=Oswald:wght@500;600;700&family=Arimo:wght@400;700&display=swap" rel="stylesheet">
<style>
  :root{
    --sky-top:#1c3b7a;
    --sky-bottom:#3170c4;
    --paper:#ffffff;
    --ink:#111111;
    --muted:#333333;
    --orange-light:#fcd27a;
    --orange-mid:#f7b445;
    --orange-deep:#f1961c;
    --blue-light:#4e9fe8;
    --blue-deep:#1452ab;
    --head-font:'Oswald', 'Arial Narrow', sans-serif;
    --body-font:'Arimo', Arial, sans-serif;
  }
  html,body{margin:0;padding:0;overflow:hidden;}
  .canvas{
    position:relative;width:818px;height:1200px;overflow:hidden;
    background:linear-gradient(180deg,var(--sky-top) 0%,var(--sky-bottom) 100%);
  }

  /* ---------- strip banners (sized by font-size = height/10) ---------- */
  .strip{
    position:absolute;height:10em;width:60em;
    background:var(--paper);box-sizing:border-box;
    border:0.15em solid var(--paper);overflow:hidden;
    box-shadow:0 0.2em 0.6em rgba(0,0,0,.25);
  }
  .strip.wide{width:64em;}
  .strip .brand{
    position:absolute;left:0;top:0;bottom:0;width:18.5em;
  }
  .strip .brand-name{
    position:absolute;left:0.8em;top:1.7em;
    font-family:var(--head-font);font-weight:700;font-size:2.6em;line-height:1;
    color:var(--ink);white-space:nowrap;
  }
  .strip .brand-tag{
    position:absolute;right:0.8em;top:6.1em;
    font-family:var(--body-font);font-weight:700;font-size:1.3em;
    color:var(--muted);white-space:nowrap;
  }
  .strip .offer{
    position:absolute;left:18.5em;right:0;top:0;bottom:0;
    background:linear-gradient(180deg,var(--orange-light) 0%,var(--orange-mid) 45%,var(--orange-deep) 100%);
  }
  .strip .headline{
    position:absolute;left:0.6em;top:0.15em;margin:0;
    font-family:var(--head-font);font-weight:600;font-size:3em;line-height:1.25;
    color:var(--ink);white-space:nowrap;
  }
  .strip .subline{
    position:absolute;left:0.35em;top:2.45em;margin:0;
    font-family:var(--body-font);font-size:1.75em;line-height:1.15;color:var(--ink);
    white-space:nowrap;
  }
  .strip .call{
    position:absolute;right:1em;bottom:0.9em;width:14.5em;height:3.2em;
    box-sizing:border-box;border:0.22em solid var(--paper);
    background:linear-gradient(180deg,var(--blue-light),var(--blue-deep));
    display:flex;align-items:center;justify-content:center;
    font-family:var(--body-font);font-weight:700;font-size:1em;color:var(--paper);
    box-shadow:0 0.1em 0.3em rgba(0,0,0,.35);
  }
  .strip .call span{font-size:1.55em;line-height:1;white-space:nowrap;}
  .strip.wide .call{right:1.2em;}

  .size-120x20{left:272px;top:87px;font-size:4px;}
  .size-168x28{left:223px;top:156px;font-size:5.7px;}
  .size-216x36{left:175px;top:246px;font-size:7.3px;}
  .size-300x50{left:89px;top:349px;font-size:10.15px;}
  .size-320x50{left:69px;top:481px;font-size:10.15px;}

  /* ---------- medium rectangle 300x250 ---------- */
  .rectangle{
    position:absolute;left:89px;top:621px;width:609px;height:507px;
    background:var(--paper);box-sizing:border-box;border:3px solid var(--paper);
    overflow:hidden;box-shadow:0 4px 12px rgba(0,0,0,.25);
  }
  .rectangle .brand{position:absolute;left:0;right:0;top:0;height:198px;}
  .rectangle .brand-name{
    position:absolute;left:46px;top:30px;
    font-family:var(--head-font);font-weight:700;font-size:88px;line-height:1;
    color:var(--ink);white-space:nowrap;
  }
  .rectangle .brand-tag{
    position:absolute;right:48px;top:148px;
    font-family:var(--body-font);font-weight:700;font-size:30px;color:var(--muted);
  }
  .rectangle .offer{
    position:absolute;left:0;right:0;top:198px;bottom:0;
    background:linear-gradient(180deg,var(--orange-light) 0%,var(--orange-mid) 45%,var(--orange-deep) 100%);
    text-align:center;
  }
  .rectangle .headline{
    margin:8px 0 0;font-family:var(--head-font);font-weight:600;font-size:46px;
    line-height:1.3;color:var(--ink);white-space:nowrap;
  }
  .rectangle .subline{
    margin:10px 0 0;font-family:var(--body-font);font-size:31px;line-height:1.2;color:var(--ink);
  }
  .rectangle .call{
    position:absolute;left:50%;bottom:22px;transform:translateX(-50%);
    width:380px;height:78px;box-sizing:border-box;border:5px solid var(--paper);
    background:linear-gradient(180deg,var(--blue-light),var(--blue-deep));
    display:flex;align-items:center;justify-content:center;
    font-family:var(--head-font);font-weight:500;font-size:46px;color:var(--paper);
    white-space:nowrap;box-shadow:0 3px 8px rgba(0,0,0,.35);
  }
</style>
</head>
<body>
<main class="canvas">

  <section class="strip size-120x20" aria-label="120 by 20 banner">
    <div class="brand"><span class="brand-name">Marlow Crest</span><span class="brand-tag">Lending Simply</span></div>
    <div class="offer">
      <p class="headline">Get Cash! Stay in Your Home!</p>
      <p class="subline">Find out if a reverse<br>mortgage is right for you!</p>
      <div class="call"><span>(888) 555-0142</span></div>
    </div>
  </section>

  <section class="strip size-168x28" aria-label="168 by 28 banner">
    <div class="brand"><span class="brand-name">Marlow Crest</span><span class="brand-tag">Lending Simply</span></div>
    <div class="offer">
      <p class="headline">Get Cash! Stay in Your Home!</p>
      <p class="subline">Find out if a reverse<br>mortgage is right for you!</p>
      <div class="call"><span>(888) 555-0142</span></div>
    </div>
  </section>

  <section class="strip size-216x36" aria-label="216 by 36 banner">
    <div class="brand"><span class="brand-name">Marlow Crest</span><span class="brand-tag">Lending Simply</span></div>
    <div class="offer">
      <p class="headline">Get Cash! Stay in Your Home!</p>
      <p class="subline">Find out if a reverse<br>mortgage is right for you!</p>
      <div class="call"><span>(888) 555-0142</span></div>
    </div>
  </section>

  <section class="strip size-300x50" aria-label="300 by 50 banner">
    <div class="brand"><span class="brand-name">Marlow Crest</span><span class="brand-tag">Lending Simply</span></div>
    <div class="offer">
      <p class="headline">Get Cash! Stay in Your Home!</p>
      <p class="subline">Find out if a reverse<br>mortgage is right for you!</p>
      <div class="call"><span>(888) 555-0142</span></div>
    </div>
  </section>

  <section class="strip wide size-320x50" aria-label="320 by 50 banner">
    <div class="brand"><span class="brand-name">Marlow Crest</span><span class="brand-tag">Lending Simply</span></div>
    <div class="offer">
      <p class="headline">Get Cash! Stay in Your Home!</p>
      <p class="subline">Find out if a reverse<br>mortgage is right for you!</p>
      <div class="call"><span>(888) 555-0142</span></div>
    </div>
  </section>

  <section class="rectangle" aria-label="300 by 250 banner">
    <div class="brand"><span class="brand-name">Marlow Crest</span><span class="brand-tag">Lending Simply</span></div>
    <div class="offer">
      <p class="headline">Get Cash! Stay in Your Home!</p>
      <p class="subline">Then below in smaller lettering<br>Find out if a reverse mortgage<br>is right for you!</p>
      <div class="call">(888) 555-0142</div>
    </div>
  </section>

</main>
</body>
</html>
```